ZorvaĀ®? Cartridge Box

Zorva is a new, patent pending nebulizer-like technology. It comes with disposable, 12 ml cartridges. We are wanting an design an outer, retail box for the cartridge. The box is white, its size is a 35mm x 35mm x 90mm, the typical size for a 30 ml boston Round tincture bottle.

```html
<!DOCTYPE html>
<html lang="en">
<head>
<meta charset="utf-8">
<title>Zorva Cartridge Box – Dieline</title>
<link rel="stylesheet" href="https://fonts.googleapis.com/css2?family=Montserrat:wght@700&family=Mulish:wght@600;700&display=swap">
<style>
  :root {
    --backdrop: #c8c7c8;
    --board: #f6f6f6;
    --glue-flap: #ececec;
    --crease: #dcdcdc;
    --brand-blue: #1fb3d4;
    --ink: #111111;
    --navy: #14213d;
  }
  html, body {
    margin: 0;
    width: 1200px;
    height: 1200px;
    overflow: hidden;
    background: var(--backdrop);
  }
  .canvas {
    width: 1200px;
    height: 1200px;
    display: flex;
    align-items: center;
    justify-content: center;
  }
  .dieline { width: 780px; height: 1034px; display: block; }
  .panel { fill: var(--board); stroke: var(--crease); stroke-width: 1; }
  .glue-flap { fill: var(--glue-flap); stroke: var(--crease); stroke-width: 1; }
  .fold { stroke: var(--crease); stroke-width: 1; }
  .brand-name {
    font-family: "Montserrat", sans-serif;
    font-weight: 700;
    fill: var(--ink);
  }
  .brand-dot { fill: var(--brand-blue); }
  .tagline {
    font-family: "Mulish", sans-serif;
    font-weight: 700;
    font-size: 8.5px;
    fill: var(--navy);
    letter-spacing: 0.2px;
  }
  .side-info {
    font-family: "Mulish", sans-serif;
    font-weight: 600;
    font-size: 8.5px;
    fill: var(--brand-blue);
    letter-spacing: 0.3px;
  }
</style>
</head>
<body>
<main class="canvas">
  <svg class="dieline" viewBox="180 573 613 812" xmlns="http://www.w3.org/2000/svg" aria-label="Zorva cartridge box dieline">
    <!-- top tuck flap and top panel -->
    <path class="panel tuck-flap" d="M336 661 V607 Q336 593 350 593 H458 Q472 593 472 607 V661 Z"/>
    <rect class="panel top-panel" x="336" y="661" width="136" height="137"/>

    <!-- dust flaps -->
    <rect class="panel dust-flap" x="200" y="730" width="136" height="68"/>
    <rect class="panel dust-flap" x="472" y="730" width="137" height="68"/>
    <rect class="panel dust-flap" x="200" y="1147" width="136" height="69"/>
    <rect class="panel dust-flap" x="472" y="1147" width="137" height="69"/>

    <!-- main panels -->
    <rect class="panel side-left" x="200" y="798" width="136" height="349"/>
    <rect class="panel front" x="336" y="798" width="136" height="349"/>
    <rect class="panel side-right" x="472" y="798" width="137" height="349"/>
    <rect class="panel back" x="609" y="798" width="137" height="349"/>

    <!-- glue flap -->
    <path class="glue-flap" d="M746 798 L773 828 V1117 L746 1147 Z"/>

    <!-- bottom panel and tuck -->
    <rect class="panel bottom-panel" x="609" y="1147" width="137" height="137"/>
    <path class="panel tuck-flap" d="M609 1284 H746 V1338 Q746 1352 732 1352 H623 Q609 1352 609 1338 Z"/>

    <!-- top panel mark -->
    <circle class="brand-dot" cx="404" cy="730" r="11"/>

    <!-- left side mark -->
    <circle class="brand-dot" cx="268" cy="973" r="12"/>

    <!-- front: brand name -->
    <text class="brand-name" font-size="52" transform="translate(390 868) rotate(90)">zorva</text>
    <circle class="brand-dot" cx="406" cy="1050" r="14"/>

    <!-- right side: mark and tagline -->
    <circle class="brand-dot" cx="500" cy="1082" r="9"/>
    <text class="tagline" x="481" y="1110">THE SAFE</text>
    <text class="tagline" x="481" y="1122">ALTERNATIVE TO</text>
    <text class="tagline" x="481" y="1134">HARMFUL VAPES</text>

    <!-- back: small brand and product info -->
    <text class="brand-name" font-size="14" transform="translate(624 815) rotate(90)">zorva</text>
    <circle class="brand-dot" cx="629" cy="870" r="4"/>
    <text class="side-info" transform="translate(714 1133) rotate(-90)">ZORVAMIST</text>
    <text class="side-info" transform="translate(725 1133) rotate(-90)">ANTI NAUSEA BLEND</text>
    <text class="side-info" transform="translate(736 1133) rotate(-90)">SAMPLE USE ONLY</text>
  </svg>
</main>
</body>
</html>
```